Redesign a Shopify Banner for a spiritual streetwear brand

Redesign Shopify banner for a brand called Vorel Studios we are a spiritually inspired streetwear brand that makes lots of designs with spiritual symbols and space aesthetics like stars. I would like the banner redesigned with the star print I included in this file in the background of the banner with our logo and tag line "spiritually inspired streetwear". you can choose a new font for the banner that could be more aesthetically pleasing. you could also included other alchemical and occult or witchy symbols on the banner along with the stars. or just create the banner with the stars I included in this file. Looking forward to see your work! Thank You.
our website right now is vorel-studios.example

```html
<!DOCTYPE html>
<html lang="en">
<head>
<meta charset="utf-8">
<title>Vorel Studios — Spiritually Inspired Streetwear</title>
<link rel="stylesheet" href="https://fonts.googleapis.com/css2?family=Marcellus&family=Quicksand:wght@300;400&display=swap">
<style>
  :root {
    --night-deep: #130e33;
    --night-indigo: #2a2384;
    --nebula-violet: #5b1f98;
    --nebula-glow: #8a2fc4;
    --star-light: rgba(255, 240, 225, 0.95);
    --star-halo: rgba(255, 200, 170, 0.35);
    --logo-white: #ffffff;
    --tagline-purple: #8b22b8;
  }
  html, body {
    margin: 0;
    padding: 0;
    width: 1200px;
    height: 629px;
    overflow: hidden;
    background: var(--night-deep);
  }
  .banner {
    position: relative;
    width: 1200px;
    height: 629px;
    overflow: hidden;
  }
  .banner__sky {
    position: absolute;
    inset: 0;
    background:
      /* glowing star points */
      radial-gradient(circle 22px at 348px 268px, var(--star-light) 0%, var(--star-halo) 25%, transparent 100%),
      radial-gradient(circle 14px at 477px 124px, var(--star-light) 0%, var(--star-halo) 30%, transparent 100%),
      radial-gradient(circle 14px at 185px 231px, var(--star-light) 0%, var(--star-halo) 30%, transparent 100%),
      radial-gradient(circle 16px at 557px 209px, var(--star-light) 0%, var(--star-halo) 30%, transparent 100%),
      radial-gradient(circle 14px at 426px 276px, var(--star-light) 0%, var(--star-halo) 30%, transparent 100%),
      radial-gradient(circle 11px at 764px 187px, var(--star-light) 0%, var(--star-halo) 30%, transparent 100%),
      radial-gradient(circle 18px at 867px 184px, var(--star-light) 0%, var(--star-halo) 28%, transparent 100%),
      radial-gradient(circle 22px at 830px 404px, var(--star-light) 0%, var(--star-halo) 25%, transparent 100%),
      radial-gradient(circle 3px at 310px 108px, rgba(230,170,255,0.8), transparent),
      radial-gradient(circle 3px at 366px 147px, rgba(230,170,255,0.7), transparent),
      radial-gradient(circle 3px at 383px 206px, rgba(230,170,255,0.7), transparent),
      radial-gradient(circle 3px at 372px 395px, rgba(230,170,255,0.6), transparent),
      radial-gradient(circle 3px at 795px 275px, rgba(230,170,255,0.6), transparent),
      /* nebula texture */
      radial-gradient(ellipse 260px 120px at 470px 150px, rgba(150, 50, 210, 0.75) 0%, transparent 80%),
      radial-gradient(ellipse 220px 90px at 820px 230px, rgba(120, 40, 190, 0.5) 0%, transparent 80%),
      radial-gradient(ellipse 300px 110px at 330px 370px, rgba(70, 50, 170, 0.6) 0%, transparent 80%),
      radial-gradient(ellipse 420px 170px at 640px 460px, rgba(50, 45, 160, 0.7) 0%, transparent 80%),
      radial-gradient(ellipse 240px 100px at 1010px 320px, rgba(90, 40, 170, 0.45) 0%, transparent 80%),
      radial-gradient(ellipse 620px 330px at 560px 250px, var(--nebula-violet) 0%, transparent 85%),
      linear-gradient(180deg, #1d1448 0%, var(--night-deep) 100%);
  }
  .brand {
    position: absolute;
    left: 0;
    right: 0;
    top: 178px;
    text-align: center;
    color: var(--logo-white);
    font-family: "Marcellus", serif;
    font-weight: 400;
    line-height: 1;
    margin: 0;
  }
  .brand__name {
    display: block;
    font-size: 124px;
    letter-spacing: 6px;
  }
  .brand__studio {
    display: block;
    margin-top: 12px;
    font-size: 56px;
    letter-spacing: 6px;
  }
  .tagline {
    position: absolute;
    left: 0;
    right: 0;
    top: 470px;
    margin: 0;
    text-align: center;
    font-family: "Quicksand", sans-serif;
    font-weight: 400;
    font-size: 51px;
    color: var(--tagline-purple);
    line-height: 1;
  }
</style>
</head>
<body>
  <main class="banner">
    <div class="banner__sky" role="img" aria-label="Purple and indigo nebula night sky scattered with glowing sparkle stars"></div>
    <h1 class="brand">
      <span class="brand__name">VOREL</span>
      <span class="brand__studio">STUDIOS</span>
    </h1>
    <p class="tagline">Spiritually Inspired Streetwear</p>
  </main>
</body>
</html>
```